Flooring Company Stationery Design Project

I need Business card, presentation folder, letterhead and envelope design.
I want the design to show a lot of creativity and that it has a modern look but still professional.
The company has a retail store but we specialize in in-home shopping.

Design must have a "flooring" company style. Creativity is going to be the main thing we'll be looking for. We want something that will stand out of the competition.

We are a remodeling busines and we want to look like one but with a good look.

PLEASE USE FOLLOWING LINK FOR ANY PHOTOS NEEDED
http://www.velmorick.com/syndicate/logos/choose_brands.html
Updates

PLEASE USE ANY PHOTOS NEEDED FROM HERE

Target Market(s)

Our target customer are 35-50 years old and decision makers are usually women

Industry/Entity Type

Retail

Requirements
Must have
• Color red
PHOTOS NEEDED CAN BE USED FROM HERE

```html
<!DOCTYPE html>
<html lang="en">
<head>
<meta charset="utf-8">
<title>Floorwell Stationery Set</title>
<link href="https://fonts.googleapis.com/css2?family=Poppins:wght@500;700&display=swap" rel="stylesheet">
<style>
  :root {
    --board: #231f20;
    --teal: #00667a;
    --teal-line: #005566;
    --red: #b0261e;
    --gold: #eda900;
    --paper: #ffffff;
  }
  html, body { margin: 0; padding: 0; width: 1200px; height: 1200px; overflow: hidden; background: var(--board); }
  .sheet { display: block; width: 1200px; height: 1200px; }
  .brand-name { font-family: "Poppins", sans-serif; font-weight: 700; fill: var(--red); }
  .brand-tagline { font-family: "Poppins", sans-serif; font-weight: 500; fill: var(--teal); }
  .card-title { font-family: "Poppins", sans-serif; font-weight: 500; fill: var(--teal); }
  .contact-line { font-family: "Poppins", sans-serif; font-weight: 500; font-size: 4.6px; fill: var(--teal); }
  .contact-label { fill: var(--gold); }
  .fold { stroke: var(--teal-line); stroke-width: 0.8; }
</style>
</head>
<body>
<svg class="sheet" viewBox="0 0 1023 1023" xmlns="http://www.w3.org/2000/svg">
  <defs>
    <clipPath id="folder-top-clip"><rect x="6" y="10" width="611" height="390"/></clipPath>
    <clipPath id="letterhead-clip"><rect x="624" y="12" width="389" height="549"/></clipPath>
    <clipPath id="envelope-clip"><rect x="480" y="808" width="476" height="201"/></clipPath>
    <clipPath id="card-front-clip"><rect x="35" y="817" width="154" height="84"/></clipPath>
    <clipPath id="card-back-clip"><rect x="227" y="819" width="154" height="85"/></clipPath>
  </defs>

  <rect class="board" width="1023" height="1023" fill="var(--board)"/>

  <!-- Presentation folder, outside -->
  <g class="folder-outside" clip-path="url(#folder-top-clip)">
    <rect x="6" y="10" width="611" height="390" fill="var(--paper)"/>
    <path d="M6,12 C150,12 220,55 300,115 C380,175 470,207 617,211" fill="none" stroke="var(--gold)" stroke-width="4"/>
    <path d="M6,19 C150,19 220,63 300,123 C380,184 470,217 617,222" fill="none" stroke="var(--teal)" stroke-width="4"/>
    <path d="M6,27 C150,27 220,72 300,132 C380,194 470,228 617,233" fill="none" stroke="var(--red)" stroke-width="5"/>
    <path d="M6,35 C150,35 220,81 300,141 C380,204 470,238 617,245 L617,400 L6,400 Z" fill="var(--teal)"/>
    <path d="M283,80 Q350,-5 470,14 Q585,45 617,205 L617,212 L512,208 Q475,70 405,45 Q330,30 283,80 Z" fill="var(--red)"/>
    <text class="brand-name" x="294" y="100" font-size="20">Floorwell</text>
    <text class="brand-tagline" x="368" y="108" font-size="5.5">Adding Value To Your Home</text>
    <line class="fold" x1="282" y1="10" x2="282" y2="400"/>
    <line class="fold" x1="556" y1="10" x2="556" y2="400"/>
    <circle cx="46" cy="206" r="12" fill="var(--board)"/>
    <circle cx="46" cy="206" r="8" fill="var(--paper)"/>
    <circle cx="46" cy="206" r="4" fill="var(--board)"/>
    <circle cx="596" cy="205" r="12" fill="var(--board)"/>
  </g>

  <!-- Presentation folder, inside -->
  <g class="folder-inside">
    <rect x="6" y="404" width="611" height="389" fill="var(--teal)"/>
    <line class="fold" x1="67" y1="404" x2="67" y2="793"/>
    <line class="fold" x1="342" y1="404" x2="342" y2="793"/>
    <circle cx="28" cy="600" r="12" fill="var(--board)"/>
    <path d="M388,692 L503,600 L617,600 L617,793 L388,793 Z" fill="var(--paper)"/>
    <text class="brand-name" x="430" y="762" font-size="24">Floorwell</text>
    <text class="brand-tagline" x="520" y="772" font-size="6">Adding Value To Your Home</text>
    <rect x="388" y="776" width="229" height="1.5" fill="var(--gold)"/>
    <rect x="388" y="779.5" width="229" height="2" fill="var(--teal)"/>
    <rect x="388" y="783" width="229" height="3" fill="var(--red)"/>
  </g>

  <!-- Letterhead -->
  <g class="letterhead" clip-path="url(#letterhead-clip)">
    <rect x="624" y="12" width="389" height="549" fill="var(--paper)"/>
    <path d="M624,48 Q700,8 830,16 Q955,28 1013,116 L902,116 Q860,45 765,38 Q680,34 624,58 Z" fill="var(--red)"/>
    <text class="brand-name" x="632" y="84" font-size="21">Floorwell</text>
    <text class="brand-tagline" x="731" y="93" font-size="6">Adding Value To Your Home</text>
    <rect x="624" y="101" width="264" height="1.5" fill="var(--gold)"/>
    <rect x="624" y="104.5" width="264" height="2" fill="var(--teal)"/>
    <rect x="624" y="109" width="264" height="4" fill="var(--red)"/>
    <rect x="624" y="535" width="389" height="2" fill="var(--gold)"/>
    <rect x="624" y="539" width="389" height="2.5" fill="var(--teal)"/>
    <rect x="624" y="544" width="389" height="4" fill="var(--red)"/>
  </g>

  <!-- Business card, front -->
  <g class="business-card-front">
    <rect x="30" y="812" width="164" height="94" fill="var(--red)"/>
    <rect x="33" y="815" width="158" height="88" fill="var(--gold)"/>
    <g clip-path="url(#card-front-clip)">
      <rect x="35" y="817" width="154" height="84" fill="var(--paper)"/>
      <path d="M35,830 Q85,814 140,822 Q175,832 189,857 L162,857 Q145,836 110,831 Q70,826 35,834 Z" fill="var(--red)"/>
      <path d="M112,901 Q165,888 181,860 L189,860 L189,901 Z" fill="var(--gold)"/>
      <rect x="35" y="851" width="106" height="1" fill="var(--gold)"/>
      <rect x="35" y="853" width="106" height="1" fill="var(--teal)"/>
      <rect x="35" y="855" width="154" height="3" fill="var(--red)"/>
    </g>
    <text class="brand-name" x="39" y="846" font-size="10">Floorwell</text>
    <text class="brand-tagline" x="88" y="846" font-size="3">Adding Value To Your Home</text>
    <text class="contact-line" x="39" y="868">48 Maple Grove Ave</text>
    <text class="contact-line" x="39" y="874"><tspan class="contact-label">Phone</tspan><tspan x="60">: 1 555 010 200</tspan></text>
    <text class="contact-line" x="39" y="880"><tspan class="contact-label">Mobile</tspan><tspan x="60">: +00 555 010 345</tspan></text>
    <text class="contact-line" x="39" y="886"><tspan class="contact-label">Email</tspan><tspan x="60">: hello@floorwell.com</tspan></text>
    <text class="contact-line" x="39" y="892"><tspan class="contact-label">Website</tspan><tspan x="60">: floorwell.com</tspan></text>
  </g>

  <!-- Business card, back -->
  <g class="business-card-back">
    <rect x="222" y="814" width="165" height="95" fill="var(--red)"/>
    <rect x="225" y="817" width="159" height="89" fill="var(--gold)"/>
    <g clip-path="url(#card-back-clip)">
      <rect x="227" y="819" width="154" height="85" fill="var(--paper)"/>
      <rect x="227" y="851" width="154" height="1.2" fill="var(--gold)"/>
      <rect x="227" y="853.5" width="154" height="1.5" fill="var(--teal)"/>
      <rect x="227" y="856.5" width="154" height="3" fill="var(--red)"/>
      <path d="M262,904 Q290,882 330,888 Q345,892 350,904 Z" fill="var(--gold)"/>
    </g>
    <text class="card-title" x="246" y="840" font-size="14">Your Text</text>
  </g>

  <!-- Envelope -->
  <g class="envelope">
    <rect x="474" y="802" width="488" height="213" fill="var(--gold)"/>
    <rect x="477" y="805" width="482" height="207" fill="var(--red)"/>
    <g clip-path="url(#envelope-clip)">
      <rect x="480" y="808" width="476" height="201" fill="var(--paper)"/>
      <path d="M480,950 Q560,895 680,893 Q800,895 870,1009 L760,1009 Q720,930 650,925 Q560,920 480,965 Z" fill="var(--red)"/>
      <rect x="480" y="999" width="270" height="1.5" fill="var(--gold)"/>
      <rect x="480" y="1002" width="270" height="2" fill="var(--teal)"/>
      <rect x="480" y="1005.5" width="270" height="3.5" fill="var(--red)"/>
    </g>
    <text class="brand-name" x="482" y="986" font-size="26">Floorwell</text>
    <text class="brand-tagline" x="582" y="995" font-size="6.5">Adding Value To Your Home</text>
  </g>
</svg>
</body>
</html>
```